Concrete Construction Business Card design

We are a commercial concrete construction company based in Texas. a family owned business which our trade was passed down and taught by our grandfather whom we want represented in this design. our grandfathers nick name was "pepe" so we are wanting the letter G to be symbolized in some way with a red pepe . colors should be possibly a grey color back ground , green letter g and red pepe pepper , to be left for you to decide with integrity , concrete professionalism,and mexican heritage

Target Market(s)

general contractors, architects,inverstors, and engineers

Industry/Entity Type

Concrete

Contact Information for Business Card

Herrera Concrete Construction LLC, Dennis Herrera, 1872 Bramblewood Ln. Cedar Hollow, OK 74012, (940)318-2746, dhslabworkllc48@quarrymail.net

```html
<!DOCTYPE html>
<html lang="en">
<head>
<meta charset="UTF-8">
<title>Herrera Concrete Construction LLC – Business Card</title>
<link rel="stylesheet" href="https://fonts.googleapis.com/css2?family=Roboto:wght@400;700&family=Source+Sans+3:wght@400;600&display=swap">
<style>
  :root {
    --page-bg: #000000;
    --card-dark-start: #4b5056;
    --card-dark-end: #18191a;
    --band-olive: #8a9678;
    --green-light: #c6e07b;
    --green-deep: #a7bb62;
    --brand-green: #b7d56c;
    --pepper-red: #c9292d;
    --ink: #484d54;
  }
  * { margin: 0; padding: 0; box-sizing: border-box; }
  html, body {
    width: 1200px;
    height: 1200px;
    overflow: hidden;
    background: var(--page-bg);
  }
  .business-card {
    position: absolute;
    left: 172px;
    top: 367px;
    width: 854px;
    height: 500px;
    overflow: hidden;
    background: linear-gradient(90deg, var(--card-dark-start), var(--card-dark-end));
  }
  .card-waves {
    position: absolute;
    inset: 0;
    width: 100%;
    height: 100%;
  }
  .brand-mark {
    position: absolute;
    left: 128px;
    top: 96px;
    width: 40px;
    height: 40px;
    border-radius: 50%;
    background: var(--pepper-red);
  }
  .company-name {
    position: absolute;
    left: 187px;
    top: 98px;
    font-family: "Roboto", Arial, sans-serif;
    font-weight: 700;
    font-size: 33px;
    color: var(--brand-green);
    white-space: nowrap;
  }
  .company-address {
    position: absolute;
    left: 226px;
    top: 150px;
    font-family: "Roboto", Arial, sans-serif;
    font-weight: 400;
    font-size: 28px;
    color: var(--brand-green);
    white-space: nowrap;
  }
  .contact {
    position: absolute;
    left: 54px;
    top: 330px;
    font-family: "Source Sans 3", "Source Sans Pro", Arial, sans-serif;
    color: var(--ink);
  }
  .contact-name {
    font-weight: 600;
    font-size: 43px;
    line-height: 52px;
  }
  .contact-line {
    font-weight: 400;
    font-size: 28px;
    line-height: 40px;
  }
</style>
</head>
<body>
  <div class="business-card">
    <svg class="card-waves" viewBox="0 0 569 333" preserveAspectRatio="none" aria-hidden="true">
      <defs>
        <linearGradient id="greenFill" x1="0" y1="0" x2="1" y2="0">
          <stop offset="0" stop-color="var(--green-light)"/>
          <stop offset="1" stop-color="var(--green-deep)"/>
        </linearGradient>
      </defs>
      <path class="wave-band" fill="var(--band-olive)"
            d="M0,95 C40,170 150,183 300,188 C430,193 525,200 569,255 L569,333 L0,333 Z"/>
      <path class="wave-green" fill="url(#greenFill)"
            d="M0,135 C55,200 180,207 300,212 C430,217 540,228 569,280 L569,333 L0,333 Z"/>
    </svg>

    <div class="brand-mark" aria-hidden="true"></div>
    <div class="company-name">Herrera Concrete Construction LLC</div>
    <div class="company-address">1872 Bramblewood Ln. Cedar Hollow, OK 74012</div>

    <div class="contact">
      <div class="contact-name">Dennis Herrera</div>
      <div class="contact-line">(940)318-2746</div>
      <div class="contact-line">dhslabworkllc48@quarrymail.net</div>
    </div>
  </div>
</body>
</html>
```